Waterjet manufacturing company needs brochure design

We need a brochure that outlines why waterjet manufacturing is beneficial for a variety of industries, our capabilities, core competencies and competitive advantages (see attached documents). The design should include our logo and include the same colours. (Dark blue RGB – 2,86,162, Light Blue RGB – 0,146,201). The design should be very clean, professional and eye catching. I've attached a few photos that can be used. Regarding the photo of the robot, please make the background white.

Manufacturing, construction, aerospace, home building

• - exact Logo colours included in design (see description)
• - booklet style design (not tri-fold)
• - professional looking
• - Logo on front cover with writing underneath:
• High Quality
• Tight Tolerance
• Components
• - Plankrow, Ropelane, Vidstow and Pixelmorra icons in Contact Us section

```html
<!DOCTYPE html>
<html lang="en">
<head>
<meta charset="utf-8">
<title>Benefits of Waterjet Cutting – Cascade Waterjet</title>
<link rel="stylesheet" href="https://fonts.googleapis.com/css2?family=Archivo+Black&family=Jost:wght@300;400;500&display=swap">
<style>
  :root {
    --dark-blue: #0256a2;
    --light-blue: #0092c9;
    --header-light: #7cc7e6;
    --card-bg: #d8eef7;
    --row-grey: #e6e7e8;
    --edm-pale: #e4f3fa;
    --ink: #111111;
    --white: #ffffff;
  }
  * { margin: 0; padding: 0; box-sizing: border-box; }
  html, body { width: 1200px; height: 848px; overflow: hidden; background: var(--white); }
  body { position: relative; font-family: "Jost", sans-serif; color: var(--ink); }

  .benefits-title {
    position: absolute; left: 26px; top: 22px;
    font-family: "Archivo Black", sans-serif;
    font-size: 24px; line-height: 26px; letter-spacing: 0.3px;
    text-transform: uppercase;
  }
  .benefits-title .brand { color: var(--dark-blue); display: block; }

  .benefit-list { position: absolute; left: 26px; top: 85px; width: 361px; list-style: none; }
  .benefit-card {
    position: relative; height: 61px; margin-bottom: 21.6px;
    background: var(--card-bg); border-radius: 16px;
    border-left: 15px solid var(--dark-blue);
    padding: 7px 14px 0 6px;
  }
  .benefit-card.tall { height: 92px; }
  .benefit-card h3 {
    font-family: "Archivo Black", sans-serif; font-weight: 400;
    font-size: 13.5px; line-height: 16px; letter-spacing: 0.2px;
  }
  .benefit-card p { font-size: 13.4px; line-height: 15.6px; margin-top: 2px; }

  .compare-title {
    position: absolute; left: 431px; width: 666px; top: 20px;
    text-align: center; font-weight: 400; font-size: 26.5px; letter-spacing: 0.3px;
  }
  .compare-title .accent { color: var(--dark-blue); }

  .compare-table {
    position: absolute; left: 431px; top: 72px; width: 666px;
    border-collapse: collapse; table-layout: fixed;
    font-size: 12.8px; line-height: 13.6px;
  }
  .compare-table col.label-col { width: 161px; }
  .compare-table th {
    height: 25px; color: var(--white); font-weight: 400; font-size: 15px;
    text-align: center; vertical-align: middle;
  }
  .compare-table th.dark { background: var(--dark-blue); }
  .compare-table th.light { background: var(--header-light); }
  .compare-table th.blank { background: var(--white); }
  .compare-table td { padding: 0 6px; vertical-align: middle; text-align: left; }
  .compare-table td.row-label { font-size: 15.5px; line-height: 16.5px; padding-left: 6px; }
  .compare-table tr.grey td { background: var(--row-grey); }
  .compare-table tr.grey td.edm { background: var(--edm-pale); }
  .compare-table tr.plain td { background: var(--white); }
  .compare-table tr.plain td.hot { background: var(--light-blue); color: var(--white); }
  .compare-table td.waterjet { border-left: 1px solid #cfd0d2; }
  .r-process { height: 83px; }
  .r-secondary { height: 126px; }
  .r-materials { height: 62px; }
  .r-thickness { height: 34px; }
  .r-accuracy { height: 37px; }
  .r-setup { height: 50px; }

  .robot-photo {
    position: absolute; left: 431px; top: 508px; width: 666px; height: 340px;
    background: linear-gradient(180deg, #b9b6ae 0%, #a7a39a 45%, #c9743e 60%, #8d8f93 78%, #7a7c80 100%);
  }
  .side-pattern {
    position: absolute; left: 1131px; top: 0; width: 69px; height: 848px;
    background: #d4d4d4;
  }
</style>
</head>
<body>

  <h1 class="benefits-title">Benefits of Waterjet Cutting<span class="brand">with Cascade Waterjet</span></h1>

  <ul class="benefit-list">
    <li class="benefit-card"><h3>VERSATILITY</h3><p>Can cut any material from 1/16th of an inch to over 20” in high or low volume</p></li>
    <li class="benefit-card"><h3>INCREASED PRODUCTIVITY</h3><p>Elimination of secondary processing increases productivity while maintaining high quality</p></li>
    <li class="benefit-card"><h3>SPEED</h3><p>Faster than conventional cutting tools for quick turnaround</p></li>
    <li class="benefit-card tall"><h3>PRECISION</h3><p>Waterjet cutting can make parts to extremely tight tolerances (Typically +/- 0.002” and as tight as +/- 0.001”). &nbsp;Precision cutting reduces scrap and raw material costs</p></li>
    <li class="benefit-card"><h3>SIMPLE</h3><p>Setup and fixturing can be completed in minutes no matter the shape, material or dimensions</p></li>
    <li class="benefit-card"><h3>COLD CUTTING PROCESS</h3><p>No heat affected zones (HAZ), stress or hardening imparted into your cut materials</p></li>
    <li class="benefit-card"><h3>SMOOTH EDGE FINISH</h3><p>No secondary finishing processes necessary unlike other conventional cutting methods</p></li>
    <li class="benefit-card"><h3>MINIMAL KERF</h3><p>High accuracy and the ability to cut endless materials means unlimited opportunities</p></li>
    <li class="benefit-card"><h3>OMNI-DIRECTIONAL CUTTING</h3><p>Allows for complex 3D designs and tight corners</p></li>
  </ul>

  <h2 class="compare-title">COMPARATIVE <span class="accent">CUTTING TECHNOLOGIES</span></h2>

  <table class="compare-table">
    <colgroup><col class="label-col"><col><col><col><col></colgroup>
    <thead>
      <tr><th class="blank"></th><th class="dark">WATERJET</th><th class="light">PLASMA</th><th class="dark">LASER</th><th class="light">EDM</th></tr>
    </thead>
    <tbody>
      <tr class="grey r-process">
        <td class="row-label">PROCESS</td>
        <td class="waterjet">Erosion using high pressure water and garnet</td>
        <td>Burning/melting using a high temperature arc</td>
        <td>Melting using a concentrated laser light beam</td>
        <td class="edm">Erosion using an electrical discharge</td>
      </tr>
      <tr class="plain r-secondary">
        <td class="row-label">SECONDARY<br>PROCESSING</td>
        <td class="waterjet">Usually none. The cold cutting process typically leaves a finished edge product ready for end use</td>
        <td class="hot">Typically yes. &nbsp;Slag grinding required for removal of HAZ and flattening to eliminate distortion from heat</td>
        <td>Sometimes yes. Required removal of oxidized edge and HAZ</td>
        <td class="hot">Usually none. &nbsp;Very shallow HAZ imparted</td>
      </tr>
      <tr class="grey r-materials">
        <td class="row-label">MATERIALS CUT</td>
        <td class="waterjet">Virtually any material</td>
        <td>Primarily steel, stainless steal and aluminum</td>
        <td>A variety of materials, but typically steel, stainless steel and aluminum</td>
        <td class="edm">Conductive materials</td>
      </tr>
      <tr class="plain r-thickness">
        <td class="row-label">THICKNESS CUT</td>
        <td class="waterjet">Up to 24”</td>
        <td class="hot">Up to 2-3”</td>
        <td>Generally 1” or less</td>
        <td class="hot">Generally 12” or less</td>
      </tr>
      <tr class="grey r-accuracy">
        <td class="row-label">ACCURACY</td>
        <td class="waterjet">Up to 0.001”</td>
        <td>Up to 0.010”</td>
        <td>Up to 0.001”</td>
        <td class="edm">Up to 0.001”</td>
      </tr>
      <tr class="plain r-setup">
        <td class="row-label">MACHINE SETUP</td>
        <td class="waterjet">Same setup for all materials</td>
        <td class="hot">Different setup for different jobs</td>
        <td>Different gasses and parameters for different jobs</td>
        <td class="hot">Different wire types for different jobs</td>
      </tr>
    </tbody>
  </table>

  <div class="robot-photo" role="img" aria-label="Photo of an orange robotic arm waterjet cutting cell over a steel cutting table in a workshop"></div>

  <div class="side-pattern" role="img" aria-label="Decorative strip of black-outlined oval tread pattern"></div>

</body>
</html>
```